Buch-Cover für Sonnenherz gesucht
Der Designer hat sich sehr schnell in meine Vorgaben eingearbeitet und gleichzeitig wertvolle Vorschläge zur Optimierung abgegeben. Das Ergebnis ist dadurch sogar besser geworden, als ich mir im Vorfeld ausgemalt hatte. 100% Weiterempfehlung.
Zielgruppe
Wir sind eine Firma die hochwertige Fitnessprodukte produziert und vertreibt. Unsere Zielgruppe sind gesundheitsbewusste Frauen ab Mitte 20 bis open end, die hohe Ansprüche an sich selbst stellen und sich für das Thema Selbstoptimierung interessieren.
Aufgabenstellung
Es soll ein Hardcover gestaltet werden.
Buchtitel: Sonnenherz, Untertitel: Das Erwachen der Seele
Detaillierte Beschreibung der Projektanforderungen siehe Anhang Projektbeschreibung. Darüber hinaus bin ich auch für alternative Gestaltungs-Ideen offen.
Das Design soll der Käuferin folgendes vermitteln:
- Wertigkeit
- Positivität
und sie ein bisschen träumen lassen und natürlich neugierig auf den Inhalt machen.

```html
<!DOCTYPE html>
<html lang="de">
<head>
<meta charset="utf-8">
<title>Sonnenherz – Buchumschlag</title>
<link href="https://fonts.googleapis.com/css2?family=Dancing+Script:wght@600;700&family=Kalam:wght@400&family=Jost:wght@400&display=swap" rel="stylesheet">
<style>
  :root {
    --gold-light: #f3e27a;
    --gold: #e7c54a;
    --amber: #d9913c;
    --cream: #f2e6cf;
    --cream-soft: #eadcc7;
    --panel: rgba(255, 255, 255, 0.32);
    --ink: #1c1a17;
    --magenta: #c6156f;
    --road-dark: #3a3a3c;
    --road-warm: #a5875a;
    --white: #ffffff;
  }
  html, body {
    margin: 0;
    padding: 0;
    width: 1200px;
    height: 887px;
    overflow: hidden;
    background: #fff;
  }
  .cover {
    position: relative;
    width: 1200px;
    height: 887px;
    overflow: hidden;
    font-family: "Jost", sans-serif;
    color: var(--ink);
  }
  .backdrop {
    position: absolute;
    inset: 0;
    background:
      radial-gradient(ellipse 520px 380px at 900px 150px, var(--gold-light) 0%, rgba(243,226,122,0) 70%),
      radial-gradient(ellipse 360px 260px at 380px 40px, #e9a24a 0%, rgba(233,162,74,0) 75%),
      radial-gradient(ellipse 300px 260px at 40px 120px, #c9932e 0%, rgba(201,147,46,0) 75%),
      linear-gradient(180deg, var(--gold) 0%, #e9c97c 35%, var(--cream) 70%, var(--cream-soft) 100%);
  }
  .back-panel {
    position: absolute;
    left: 33px;
    top: 75px;
    width: 489px;
    height: 626px;
    background: var(--panel);
    border-radius: 6px;
  }
  .back-heading {
    position: absolute;
    left: 33px;
    top: 116px;
    width: 489px;
    margin: 0;
    text-align: center;
    font-family: "Kalam", cursive;
    font-weight: 400;
    font-size: 36px;
    line-height: 1;
  }
  .blurb {
    position: absolute;
    left: 47px;
    top: 205px;
    width: 461px;
    font-size: 16.6px;
    line-height: 22.2px;
    text-align: justify;
  }
  .blurb p { margin: 0 0 22px; }
  .barcode-area {
    position: absolute;
    left: 308px;
    top: 714px;
    width: 221px;
    height: 132px;
    background: var(--white);
  }
  .spine-title {
    position: absolute;
    left: 600px;
    top: 212px;
    transform-origin: 0 0;
    transform: rotate(90deg) translateY(-50%);
    white-space: nowrap;
    display: flex;
    align-items: baseline;
    gap: 10px;
  }
  .spine-title .title {
    font-family: "Dancing Script", cursive;
    font-weight: 700;
    font-size: 40px;
    color: var(--magenta);
  }
  .spine-title .sub {
    font-family: "Kalam", cursive;
    font-size: 25px;
  }
  .imprint {
    position: absolute;
    left: 560px;
    top: 812px;
    width: 80px;
    display: flex;
    align-items: center;
    justify-content: center;
    gap: 5px;
    font-size: 12px;
    color: var(--ink);
  }
  .imprint .dot {
    width: 9px;
    height: 9px;
    border-radius: 50%;
    background: var(--gold);
  }
  .front-photo {
    position: absolute;
    left: 639px;
    top: 477px;
    width: 561px;
    height: 410px;
    background:
      radial-gradient(ellipse 200px 170px at 430px 150px, rgba(227,176,110,0.85) 0%, rgba(227,176,110,0) 80%),
      linear-gradient(180deg, var(--road-dark) 0%, var(--road-warm) 45%, #6f6450 70%, #2e2d30 100%);
  }
  .front-title {
    position: absolute;
    left: 655px;
    top: 155px;
    width: 545px;
    margin: 0;
    text-align: center;
    font-family: "Dancing Script", cursive;
    font-weight: 700;
    font-size: 104px;
    line-height: 1;
    color: var(--magenta);
  }
  .front-subtitle {
    position: absolute;
    left: 655px;
    top: 305px;
    width: 545px;
    text-align: center;
    font-family: "Kalam", cursive;
    font-size: 26px;
    line-height: 1;
  }
</style>
</head>
<body>
<main class="cover">
  <div class="backdrop" role="img" aria-label="Warmer goldener Hintergrund mit weichen Lichtkreisen"></div>

  <section class="back-cover">
    <div class="back-panel"></div>
    <h2 class="back-heading">« Was zählt wirklich? »</h2>
    <div class="blurb">
      <p>Ich habe mich oft gefragt: Wie soll ich bloß die Liebe und Bestätigung, die mir damals in meiner Kindheit verwehrt blieben, „nachholen“? Lösungsansätze für mein Problem hatte ich in der Vergangenheit durchaus: Ich versuchte das Loch in mir mit Hilfe zur Selbsthilfe, Erfolg im Job und Konsum zu stopfen. Und meine Partner mussten auch für so einiges herhalten.</p>
      <p>Von Gott wollte ich lange nichts wissen. Schließlich hatte er es zugelassen, dass mir sehr viel Unheil in meinem Leben widerfahren ist. Und deshalb war ich echt wütend auf ihn.</p>
      <p>Heutzutage bin ich mir sicher, dass ich mit dieser Denkweise meine Lebenszeit verschwendet habe. Letzten Sommer begriff ich endlich: im Leben gilt die gleiche Gesetzmäßigkeit wie beim Autofahren. Der Rückspiegel ist so klein und die Frontscheibe so groß, weil das, was vor uns liegt, viel wichtiger ist als das, was hinter uns liegt. Aufgrund dieser Erkenntnis entschied ich mich, einen völlig neuen Weg einzuschlagen und wagte mich auf eine spannende Reise, die mein Leben für immer veränderte …</p>
    </div>
    <div class="barcode-area"></div>
  </section>

  <section class="spine">
    <div class="spine-title">
      <span class="title">Sonnenherz</span>
      <span class="sub">– Das Erwachen der Seele</span>
    </div>
    <div class="imprint"><span class="dot"></span>Lichtweg</div>
  </section>

  <section class="front-cover">
    <h1 class="front-title">Sonnenherz</h1>
    <div class="front-subtitle">Das Erwachen der Seele</div>
    <div class="front-photo" role="img" aria-label="Foto: Frau mit Sonnenbrille am Steuer eines Cabrios, Blick auf eine sonnige Landstraße"></div>
  </section>
</main>
</body>
</html>
```